Law Firm Ad

We need a magazine/auction program design for a Sacramento based law firm. Current need is for a school auction sponsorship. Ad must be 5 1/2 x 8 1/2 in high resolution (300 dpi) and in JPG or PDF format. A clean, modern, simple design is preferred.

Thornby Law Corporation provides general preventative employment advice to employers in avoiding litigation and has counseled businesses on cases involving employment law, unfair business practices and trade secrets. Thornby Law Corporation also practices in business, real estate and employment litigation.

Target Market(s)

This particular ad it is to support Haskeldale Elementary School's 21st Annual Auction and Dinner on March 14, 2015.
Here's the facebook link https://www.examplesocial.test/HaskeldaleAuction/photos/a.918273645012398.275103.610294857361042/3049182736450192/?type=1&theater
But I would like something that might be fairly universal.

Industry/Entity Type

Real Estate

Font styles to use
Sans Serif

Requirements
Must have
• Clean and crisp design. Not overly traditional.
Nice to have
• Contact information:
Thornby Law Corporation
318 Brimley Avenue, Suite 200
Sacramento, CA 95000
916.555.0142
thornby-law.test

```html
<!DOCTYPE html>
<html lang="en">
<head>
<meta charset="utf-8">
<title>Thornby Law Corporation – Sponsor Ad</title>
<link rel="stylesheet" href="https://fonts.googleapis.com/css2?family=Nunito+Sans:wght@400;600;700;800&display=swap">
<style>
  :root {
    --red: #e8141c;
    --orange: #f37a21;
    --amber: #f7941d;
    --white: #ffffff;
    --ink: #2b0f08;
    --cream: #f3d08e;
    --honey: #d99a5a;
    --brick: #a9513a;
    --walnut: #6b3420;
    --espresso: #1c0b06;
    --silver: #b8ab9a;
  }
  html, body {
    margin: 0;
    padding: 0;
    width: 900px;
    height: 1200px;
    overflow: hidden;
    background: var(--white);
  }
  .ad {
    position: relative;
    width: 900px;
    height: 1200px;
    overflow: hidden;
    font-family: "Nunito Sans", "Helvetica Neue", Arial, sans-serif;
    background: var(--white);
  }
  .band { position: absolute; left: 0; width: 900px; }
  .band--top-red    { top: 0;    height: 18px; background: var(--red); }
  .band--top-orange { top: 20px; height: 9px;  background: var(--amber); }
  .band--rule       { top: 309px; height: 11px; background: var(--amber); }

  .masthead {
    position: absolute;
    top: 29px; left: 0;
    width: 900px; height: 280px;
    display: flex; flex-direction: column;
    align-items: center; justify-content: center;
    color: var(--amber);
    font-weight: 700;
  }
  .masthead__name { font-size: 150px; line-height: 0.95; letter-spacing: -3px; }
  .masthead__sub  { font-size: 56px; line-height: 1.1; letter-spacing: 2px; margin-top: 10px; }

  .hero {
    position: absolute;
    top: 320px; left: 0;
    width: 900px; height: 735px;
    background:
      radial-gradient(ellipse 26% 48% at 68% 52%, rgba(200,190,175,0.55), transparent 70%),
      radial-gradient(ellipse 30% 12% at 62% 78%, rgba(190,175,160,0.45), transparent 70%),
      linear-gradient(172deg, transparent 66%, rgba(110,55,30,0.85) 70%, var(--walnut) 80%, var(--espresso) 100%),
      linear-gradient(90deg, rgba(28,11,6,0.55) 0%, transparent 40%),
      linear-gradient(180deg, var(--cream) 0%, var(--honey) 14%, var(--brick) 40%, #8a3f2a 60%, var(--walnut) 100%);
  }

  .contact {
    position: absolute;
    left: 25px; top: 851px;
    margin: 0;
    color: var(--white);
    font-style: normal;
    font-weight: 600;
    font-size: 24px;
    line-height: 31px;
  }
  .contact p { margin: 0; }
  .contact .contact__phone { margin-top: 22px; }
  .contact .contact__web   { margin-top: 11px; }

  .band--thin-orange { top: 1055px; height: 8px;  background: var(--amber); }
  .band--thin-red    { top: 1069px; height: 8px;  background: var(--red); }
  .band--block       { top: 1077px; height: 110px; background: var(--orange); }
  .band--base-red    { top: 1188px; height: 12px; background: var(--red); }

  .footer-mark {
    position: absolute;
    right: 52px; top: 1080px;
    text-align: center;
    color: var(--ink);
    font-weight: 700;
  }
  .footer-mark__name { font-size: 58px; line-height: 1; letter-spacing: -1px; }
  .footer-mark__sub  { font-size: 23px; line-height: 1.2; letter-spacing: 1.5px; margin-top: 6px; }
</style>
</head>
<body>
  <div class="ad">
    <div class="band band--top-red"></div>
    <div class="band band--top-orange"></div>

    <header class="masthead">
      <div class="masthead__name">Thornby</div>
      <div class="masthead__sub">LAW CORPORATION</div>
    </header>

    <div class="band band--rule"></div>

    <div class="hero" role="img" aria-label="Photograph of ornate silver scales of justice standing on a polished wooden table, with blurred courtroom benches behind"></div>

    <address class="contact">
      <p>Thornby Law Corporation</p>
      <p>318 Brimley Avenue, Suite 200</p>
      <p>Sacramento, CA 95000</p>
      <p class="contact__phone">916.555.0142</p>
      <p class="contact__web">thornby-law.test</p>
    </address>

    <div class="band band--thin-orange"></div>
    <div class="band band--thin-red"></div>
    <div class="band band--block"></div>
    <div class="band band--base-red"></div>

    <div class="footer-mark">
      <div class="footer-mark__name">Thornby</div>
      <div class="footer-mark__sub">LAW CORPORATION</div>
    </div>
  </div>
</body>
</html>
```